Game, Voice & Dedicated Server Company Needs a Business Card Design

We need a new business card design, centered around our new logo (PSD provided below).

Designs that we do like:
https://pixelmarsh.net/item/corporate-business-card/5382017?s_rank=43 (needs to be made more eye catching)

Our main areas of business are:
- Dedicated Servers
- Game Servers
- Voice Servers
- Mitigation Security Specialists

Industry/Entity Type

Business

Contact Information for Business Card

On the card: (and anything else you would suggest)
- Staff member name
- Staff member position in company
- Staff member phone number
- Staff member email
- Other / Staff member Voicelink
- Website link

Colors
9bcb3c
abd036

Requirements
Must have
• Design of Card:
• - Green (same green as the logo)
• - Business / Corporate design
• - Something a little different / abstract that shouts premium

```html
<!DOCTYPE html>
<html lang="en">
<head>
<meta charset="utf-8">
<title>Brightpath Hosting – Business Card</title>
<link rel="stylesheet" href="https://fonts.googleapis.com/css2?family=Saira+Condensed:wght@500&family=Montserrat:wght@300;400;700&display=swap">
<style>
  :root {
    --page: #ffffff;
    --card-dark: #2a2a2a;
    --card-light: #313131;
    --green: #8dc63f;
    --white: #ffffff;
  }
  * { box-sizing: border-box; margin: 0; padding: 0; }
  html, body { width: 1200px; height: 1003px; overflow: hidden; background: var(--page); }
  .canvas { position: relative; width: 1200px; height: 1003px; }

  .card { position: absolute; overflow: hidden; background: var(--card-dark); }
  .card-front { left: 225px; top: 51px; width: 768px; height: 438px; }
  .card-back  { left: 225px; top: 513px; width: 770px; height: 440px; }

  .front-diagonal { position: absolute; inset: 0; }

  .front-brand {
    position: absolute; left: 0; right: 0; top: 170px;
    text-align: center;
    font-family: "Montserrat", sans-serif; font-weight: 700;
    font-size: 44px; letter-spacing: 1px; line-height: 1.1;
    color: var(--green); text-transform: uppercase;
  }
  .front-url {
    position: absolute; left: 0; right: 0; top: 345px;
    text-align: center;
    font-family: "Saira Condensed", sans-serif; font-weight: 500;
    font-size: 25px; color: var(--white);
  }

  .back-frame { position: absolute; inset: 0; }
  .back-brand {
    position: absolute; left: 52px; width: 240px; top: 195px;
    text-align: center;
    font-family: "Montserrat", sans-serif; font-weight: 700;
    font-size: 27px; line-height: 1.05; letter-spacing: -0.5px;
    color: var(--green); text-transform: uppercase;
  }
  .back-brand-mark {
    position: absolute; left: 147px; top: 128px;
    width: 50px; height: 50px; border-radius: 50%;
    background: var(--green);
  }

  .contact { position: absolute; left: 310px; right: 0; top: 0; text-align: center; color: var(--white); }
  .contact-name {
    position: absolute; left: 0; right: 0; top: 40px;
    font-family: "Saira Condensed", sans-serif; font-weight: 500;
    font-size: 68px; line-height: 1;
  }
  .contact-role {
    position: absolute; left: 0; right: 0; top: 120px;
    font-family: "Montserrat", sans-serif; font-weight: 300;
    font-size: 21px; color: var(--green);
  }
  .contact-phones {
    position: absolute; left: 0; right: 0; top: 192px;
    font-family: "Montserrat", sans-serif; font-weight: 300;
    font-size: 21px; line-height: 30px;
  }
  .contact-email {
    position: absolute; left: 0; right: 0; top: 292px;
    font-family: "Montserrat", sans-serif; font-weight: 300; font-size: 21px;
  }
  .contact-chat {
    position: absolute; left: 0; right: 0; top: 351px;
    font-family: "Montserrat", sans-serif; font-weight: 300; font-size: 21px;
    display: flex; justify-content: center; align-items: center; gap: 14px;
  }
  .chat-dot { width: 26px; height: 26px; border-radius: 50%; background: var(--green); }
</style>
</head>
<body>
<main class="canvas">

  <section class="card card-front" aria-label="Card front">
    <svg class="front-diagonal" width="768" height="438" viewBox="0 0 768 438" aria-hidden="true">
      <polygon points="768,0 768,438 0,438" fill="var(--card-light)"/>
    </svg>
    <div class="front-brand">Brightpath<br>Hosting</div>
    <div class="front-url">brightpath-hosting.com</div>
  </section>

  <section class="card card-back" aria-label="Card back">
    <svg class="back-frame" width="770" height="440" viewBox="0 0 770 440" aria-hidden="true">
      <polyline points="120,0 120,75 50,125 50,315 120,367 120,440" fill="none" stroke="var(--green)" stroke-width="3"/>
      <polyline points="218,0 218,75 288,125 288,315 218,367 218,440" fill="none" stroke="var(--green)" stroke-width="3"/>
    </svg>
    <div class="back-brand-mark" aria-hidden="true"></div>
    <div class="back-brand">Brightpath<br>Hosting</div>

    <div class="contact">
      <div class="contact-name">John Doe</div>
      <div class="contact-role">Creative Director</div>
      <div class="contact-phones">(o)&nbsp; +61 0000 0000<br>(c)&nbsp; +61 0000 0000</div>
      <div class="contact-email">JohnDoe@Brightpath-Hosting.com</div>
      <div class="contact-chat"><span class="chat-dot" aria-hidden="true"></span>Staff Member Voicelink</div>
    </div>
  </section>

</main>
</body>
</html>
```